Online Home Automation business needs business card design

New business starting up that sells home-automation products in Australia. Business card needs to look very polished and professional. The business name is "Vesk Automation".
Updates

Thank you all for the great designs, We are really impressed. We are in the process of deciding on a design but keep the designs coming in.

Industry/Entity Type

Business

```html
<!DOCTYPE html>
<html lang="en">
<head>
<meta charset="utf-8">
<title>Vesk Automation – Business Card</title>
<link rel="stylesheet" href="https://fonts.googleapis.com/css2?family=Poppins:wght@300;400;700&display=swap">
<style>
  :root {
    --page-bg: #2b2a28;
    --brand-red: #e8222b;
    --brand-black: #0c0c0c;
    --card-light: #ececec;
    --ink: #1a1a1a;
    --ink-soft: #3a3a3a;
    --rule: #555555;
    --decor-grey: #d6d6d6;
    --decor-warm: #e6d3c8;
  }
  * { box-sizing: border-box; margin: 0; padding: 0; }
  html, body {
    width: 1200px; height: 757px; overflow: hidden;
    background: var(--page-bg);
    font-family: "Poppins", sans-serif;
  }
  .canvas {
    position: relative; width: 1200px; height: 757px;
    display: flex; align-items: center; justify-content: center; gap: 60px;
  }
  .card {
    position: relative; width: 500px; height: 300px; overflow: hidden;
    border-radius: 4px;
    box-shadow: 0 14px 30px rgba(0,0,0,.45);
  }

  /* Front */
  .card-front { background: var(--brand-red); }
  .front-artwork {
    position: absolute; left: 0; right: 0; top: 120px; bottom: 0;
    background: linear-gradient(135deg, var(--brand-black) 0%, #1a0a0b 55%, #5a1013 100%);
  }
  .card-front .wordmark {
    position: absolute; top: 24px; right: 42px;
    color: var(--brand-black); line-height: 1;
  }
  .wordmark .name-strong { display: block; font-weight: 700; font-size: 36px; }
  .wordmark .name-light { display: block; font-weight: 300; font-size: 34px; margin-top: 2px; }

  /* Back */
  .card-back { background: var(--card-light); }
  .back-decor {
    position: absolute; right: 0; top: 0; bottom: 0; width: 220px;
    background: linear-gradient(160deg, var(--decor-grey) 0%, var(--decor-warm) 60%, var(--decor-grey) 100%);
    opacity: .8;
  }
  .back-brand {
    position: absolute; left: 34px; top: 108px;
    display: flex; align-items: center; gap: 12px; color: var(--ink);
  }
  .brand-dot { width: 50px; height: 50px; border-radius: 50%; background: var(--brand-red); }
  .back-brand .wordmark { line-height: 1; }
  .back-brand .name-strong { font-size: 28px; }
  .back-brand .name-light { font-size: 27px; }
  .holder-name {
    position: absolute; right: 34px; top: 34px;
    font-size: 18px; font-weight: 400; letter-spacing: .5px; color: var(--ink);
  }
  .holder-rule {
    position: absolute; right: 34px; top: 62px; width: 240px; height: 1px; background: var(--rule);
  }
  .contact-rule {
    position: absolute; left: 34px; bottom: 96px; width: 260px; height: 1px; background: var(--rule);
  }
  .contact-list {
    position: absolute; left: 34px; bottom: 24px; list-style: none;
    font-size: 13px; color: var(--ink-soft); line-height: 22px;
  }
  .contact-list li { display: flex; align-items: center; gap: 10px; }
  .contact-icon {
    width: 14px; height: 14px; border-radius: 3px; background: var(--brand-red);
    display: inline-flex; align-items: center; justify-content: center;
  }
</style>
</head>
<body>
<main class="canvas">

  <section class="card card-front" aria-label="Card front">
    <div class="front-artwork" role="img" aria-label="Large brand illustration in black, red and silver"></div>
    <div class="wordmark">
      <span class="name-strong">Vesk</span>
      <span class="name-light">Automation</span>
    </div>
  </section>

  <section class="card card-back" aria-label="Card back">
    <div class="back-decor" role="img" aria-label="Faint brand illustration in grey and peach tones"></div>
    <p class="holder-name">TOBIN HALE</p>
    <div class="holder-rule"></div>

    <div class="back-brand">
      <span class="brand-dot"></span>
      <div class="wordmark">
        <span class="name-strong">Vesk</span>
        <span class="name-light">Automation</span>
      </div>
    </div>

    <div class="contact-rule"></div>
    <ul class="contact-list">
      <li>
        <span class="contact-icon">
          <svg width="9" height="9" viewBox="0 0 10 10" aria-hidden="true"><path d="M2 1 L4 1 L5 3 L4 4 C4.5 5 5 5.5 6 6 L7 5 L9 6 L9 8 C6 9 1 4 2 1 Z" fill="#fff"/></svg>
        </span>
        +61 400 555 019
      </li>
      <li>
        <span class="contact-icon">
          <svg width="9" height="9" viewBox="0 0 10 10" aria-hidden="true"><rect x="1" y="2.5" width="8" height="5" fill="none" stroke="#fff" stroke-width="1"/><path d="M1 2.5 L5 5.5 L9 2.5" fill="none" stroke="#fff" stroke-width="1"/></svg>
        </span>
        info@veskautomation.com.au
      </li>
      <li>
        <span class="contact-icon">
          <svg width="9" height="9" viewBox="0 0 10 10" aria-hidden="true"><path d="M2 5 L8 5 M5.5 2.5 L8 5 L5.5 7.5" fill="none" stroke="#fff" stroke-width="1.3"/></svg>
        </span>
        www.veskautomation.com
      </li>
    </ul>
  </section>

</main>
</body>
</html>
```